Our new beauty salon requires a price list brochure

Our beauty clinic is a medical grade skin care clinic. So our salon is very clinical and professional in appearance. I would like the colours to be similar to our logo design with some nice texture or abstract shapes thrown in.
Pricelist, contact details and logo is attached
I would prefer it to be a 3 fold brochure.

Target Market(s)

Females aged 30-50

Colors
85acd3
cedeed
c4c4c4
5c5c5c
000000
ffffff
eea3c7
f9d9e8
dbdbdb

Requirements
Must have
• easy to read

```html
<!DOCTYPE html>
<html lang="en">
<head>
<meta charset="utf-8">
<title>Lumera Aesthetics – Price List</title>
<link href="https://fonts.googleapis.com/css2?family=Jost:wght@300;400;500;600;700&display=swap" rel="stylesheet">
<style>
:root{
  --stage:#3f3f41;
  --green:#6cbd3b;
  --slate:#505c68;
  --text:#5b6570;
  --line:#98a2ab;
  --sheet-a:#cfe9ec;
  --sheet-b:#eef3f5;
  --dark-row:#4d5a66;
  --dark-tag:#2e343a;
}
*{box-sizing:border-box;margin:0;padding:0}
html,body{width:800px;height:1200px;overflow:hidden;background:var(--stage)}
body{font-family:"Jost",sans-serif;color:var(--text);position:relative}
.sheet{position:absolute;left:30px;width:740px;height:560px;display:flex;
  background:linear-gradient(160deg,var(--sheet-a) 0%,#e3f0f2 45%,var(--sheet-b) 100%);
  border-bottom:3px solid var(--green)}
.sheet.outside{top:25px}
.sheet.inside{top:615px}
.panel{width:246.6px;height:100%;padding:26px 18px 18px;position:relative;border-right:1px solid rgba(120,140,150,.18)}
.panel:last-child{border-right:none}
.heading{font-size:14px;font-weight:400;letter-spacing:.3px;color:var(--slate);text-transform:uppercase}
.heading b{font-weight:700}
.heading .mixed{text-transform:none;font-size:15px}
.rule{width:18px;height:3px;background:var(--green);margin:5px 0 12px}
.row{position:relative;height:16px;margin-bottom:2px}
.row .label{height:13px;margin-top:3px;border:1px solid var(--line);border-radius:3px;background:rgba(255,255,255,.55);
  font-size:8.5px;line-height:11px;padding-left:14px;color:var(--slate);margin-right:6px;white-space:nowrap;overflow:hidden}
.row .price{position:absolute;right:0;top:0;width:38px;height:12px;background:var(--green);color:#fff;
  font-size:8.5px;font-weight:600;line-height:12px;text-align:center;border-radius:2px}
.gap{height:8px}
.row.dark .label{background:var(--dark-row);border-color:var(--dark-row);color:#fff}
.row .price.wide{width:78px}
.row .price.tag{background:var(--dark-tag);right:42px;width:34px}
.duration{height:12px;margin-bottom:4px;position:relative}
.duration span{position:absolute;right:0;top:0;width:38px;height:12px;background:var(--green);color:#fff;
  font-size:8.5px;font-weight:600;line-height:12px;text-align:center;border-radius:2px}
.note{font-size:8.5px;line-height:11px;color:var(--slate);margin:6px 0 4px}
.note b{font-weight:700}
.contact{text-align:center;position:absolute;left:0;right:0;bottom:46px;font-size:8px;line-height:12px;color:var(--slate)}
.contact .name{font-size:14px;letter-spacing:.6px;margin-bottom:8px}
.contact .ico{display:inline-block;width:8px;height:8px;border-radius:50%;background:var(--green);vertical-align:middle;margin-right:4px}
.contact .block{margin-bottom:6px}
.brand{text-align:center;margin-top:4px}
.brand .word{font-size:34px;font-weight:300;letter-spacing:6px;color:var(--slate);line-height:1}
.brand .sub{font-size:7px;letter-spacing:4px;color:var(--slate)}
.photo{position:absolute;border-radius:4px}
.photo.cover{left:18px;right:0;top:110px;bottom:60px;background:linear-gradient(180deg,#e6eef0,#d9c2b6 60%,#f2efee)}
.photo.legs{left:0;right:20px;bottom:8px;height:92px;background:linear-gradient(90deg,#eef2f3,#e4b9a0 55%,#eef2f3)}
.photo.smile{left:40px;right:0;bottom:14px;height:150px;background:radial-gradient(ellipse at 55% 45%,#dcb3a0,#e9e4e3 70%)}
.treat{font-size:9px;line-height:12px;color:var(--slate);margin-bottom:6px}
.treat b{font-weight:700}
.treat .amt{font-weight:700;font-size:10px}
</style>
</head>
<body>

<section class="sheet outside">
  <div class="panel">
    <h2 class="heading">IPL <b>Hair Removal</b></h2>
    <div class="rule"></div>
    <div class="row"><div class="label">Upper Lip</div><div class="price">$50</div></div>
    <div class="row"><div class="label">Chin</div><div class="price">$50</div></div>
    <div class="row"><div class="label">Cheeks</div><div class="price">$75</div></div>
    <div class="row"><div class="label">Whole Face</div><div class="price">$350</div></div>
    <div class="gap"></div>
    <div class="row"><div class="label">Bikini</div><div class="price">$90</div></div>
    <div class="row"><div class="label">G String</div><div class="price">$120</div></div>
    <div class="row"><div class="label">Brazilian</div><div class="price">$150</div></div>
    <div class="gap"></div>
    <div class="row"><div class="label">Underarms</div><div class="price">$90</div></div>
    <div class="row"><div class="label">Half Arm</div><div class="price">$180</div></div>
    <div class="row"><div class="label">Full Arm</div><div class="price">$250</div></div>
    <div class="row"><div class="label">Half Leg</div><div class="price">$290</div></div>
    <div class="row"><div class="label">Thighs</div><div class="price">$290</div></div>
    <div class="row"><div class="label">Full Leg</div><div class="price">$490</div></div>
    <div class="gap"></div>
    <div class="row"><div class="label">Full Back</div><div class="price">$350</div></div>
    <div class="row"><div class="label">Shoulders</div><div class="price">$180</div></div>
    <div class="row"><div class="label">Nipples</div><div class="price">$60</div></div>
    <div class="row"><div class="label">Snail Trail</div><div class="price">$50</div></div>
    <div class="row"><div class="label">Stomach</div><div class="price">$250</div></div>
    <div class="row"><div class="label">Chest</div><div class="price">$250</div></div>
    <div class="row"><div class="label">Buttocks</div><div class="price">$200</div></div>
  </div>

  <div class="panel">
    <h2 class="heading">IPL <b>Photo Rejuvenation</b></h2>
    <div class="rule"></div>
    <div class="row"><div class="label">Full face</div><div class="price">$350</div></div>
    <div class="row"><div class="label">Neck</div><div class="price">$200</div></div>
    <div class="row"><div class="label">Face, neck and décolletage</div><div class="price">$450</div></div>
    <div class="row"><div class="label">Spot Treatment</div><div class="price">$50</div></div>
    <div class="gap"></div><div class="gap"></div>
    <h2 class="heading"><b>Tinting</b></h2>
    <div class="rule"></div>
    <div class="row"><div class="label">Eyelash Tint</div><div class="price">$5</div></div>
    <div class="row"><div class="label">Lash Lift and Tint</div><div class="price">$21</div></div>
    <div class="row"><div class="label">Henna eyebrows and wax</div><div class="price">$20</div></div>
    <div class="row"><div class="label">Eyelash Tint and brow wax</div><div class="price">$45</div></div>

    <div class="contact">
      <div class="name">LUMERA AESTHETICS</div>
      <div class="block"><svg width="12" height="12" viewBox="0 0 12 12"><circle cx="6" cy="6" r="5.5" fill="none" stroke="#6cbd3b"/><path d="M6 2.8a2 2 0 0 1 2 2c0 1.5-2 4-2 4s-2-2.5-2-4a2 2 0 0 1 2-2z" fill="#6cbd3b"/></svg><br>4/28 Coral Bay Road<br>Seabreeze Point<br>Western Australia</div>
      <div class="block"><svg width="9" height="9" viewBox="0 0 10 10"><path d="M2 1l2 2-1 1.5a6 6 0 0 0 2.5 2.5L7 6l2 2-1.5 1.5C4 9 1 6 .5 2.5z" fill="#6cbd3b"/></svg> (08) 5550 1234</div>
      <div><span class="ico"></span>www.lumeraskin.com.au</div>
      <div><span class="ico"></span>lumera_skin</div>
      <div><span class="ico"></span>lumera skin australia</div>
    </div>
  </div>

  <div class="panel">
    <div class="brand">
      <div class="word">lumera</div>
      <div class="sub">AESTHETICS</div>
    </div>
    <div class="photo cover" role="img" aria-label="Portrait photo of a woman with smooth skin, hand resting on her cheek"></div>
  </div>
</section>

<section class="sheet inside">
  <div class="panel">
    <h2 class="heading"><b>Waxing</b></h2>
    <div class="rule"></div>
    <div class="row"><div class="label">Eyebrow</div><div class="price">$21</div></div>
    <div class="row"><div class="label">Lip</div><div class="price">$15</div></div>
    <div class="row"><div class="label">Chin</div><div class="price">$15</div></div>
    <div class="row"><div class="label">Sides Of Face</div><div class="price">$20</div></div>
    <div class="row"><div class="label">Underarm</div><div class="price">$20</div></div>
    <div class="row"><div class="label">Forearm</div><div class="price">$25</div></div>
    <div class="row"><div class="label">Full Arm</div><div class="price">$35</div></div>
    <div class="row"><div class="label">Lower Leg</div><div class="price">$30</div></div>
    <div class="row"><div class="label">Upper Leg</div><div class="price">$30</div></div>
    <div class="row"><div class="label">Full Leg</div><div class="price">$50</div></div>
    <div class="row"><div class="label">Inner Thigh</div><div class="price">$10</div></div>
    <div class="row"><div class="label">Snail Trail</div><div class="price">$10</div></div>
    <div class="row"><div class="label">Bikini</div><div class="price">$30</div></div>
    <div class="row"><div class="label">G String</div><div class="price">$40</div></div>
    <div class="row"><div class="label">Brazilian</div><div class="price">$50</div></div>
    <div class="gap"></div>
    <div class="row"><div class="label">Eyebrow Wax And Lip Wax</div><div class="price">$30</div></div>
    <div class="row"><div class="label">Eyebrow, Lip And Chin Wax</div><div class="price">$45</div></div>
    <div class="photo legs" role="img" aria-label="Photo of smooth bare legs"></div>
  </div>

  <div class="panel">
    <h2 class="heading">Mens <b>Waxing</b></h2>
    <div class="rule"></div>
    <div class="row"><div class="label">Mono brow</div><div class="price">$5</div></div>
    <div class="row"><div class="label">Eyebrow</div><div class="price">$21</div></div>
    <div class="row"><div class="label">Neck</div><div class="price">$20</div></div>
    <div class="row"><div class="label">Full back</div><div class="price">$45</div></div>
    <div class="row"><div class="label">Chest and Abdomen</div><div class="price">$45</div></div>
    <div class="gap"></div>
    <div class="row dark"><div class="label">Lumera Mini Facial</div><div class="price tag">$80</div><div class="price">40min</div></div>
    <div class="row dark"><div class="label">Lumera Deluxe Facial</div><div class="price tag">$110</div><div class="price">1 hour</div></div>
    <div class="row dark"><div class="label">Microdermabrasion</div><div class="price">$125</div></div>
    <div class="row dark"><div class="label">Mini Micro</div><div class="price">$80</div></div>
    <div class="row dark"><div class="label">Wrinkle Relaxers</div><div class="price wide">$175 per area</div></div>
    <p class="note">(Crows, frown lines, forehead lines)<br>or all <b>3 areas for $450</b></p>
    <p class="note"><b>$50</b> minor areas<br>(Gummy smile, brow lift, bunny lines)</p>
    <div class="row dark"><div class="label">Dermal &amp; Lip Fillers</div><div class="price wide">$500 per ml</div></div>
    <div class="gap"></div>
    <h2 class="heading"><span class="mixed">Chemical <b>Peels</b></span></h2>
    <div class="rule"></div>
    <div class="duration"><span>30min</span></div>
    <div class="row"><div class="label">Clarix Dr Peels</div><div class="price">$120</div></div>
    <div class="row"><div class="label">Lactic Acid Peels 20%/40%/60%</div><div class="price">$120</div></div>
    <div class="row"><div class="label">Renewal Peel</div><div class="price">$120</div></div>
    <div class="row"><div class="label">Even Tone Peel</div><div class="price">$120</div></div>
    <div class="row"><div class="label">Clear Skin Peel</div><div class="price">$120</div></div>
  </div>

  <div class="panel">
    <div class="duration"><span>30min</span></div>
    <div class="row"><div class="label">Solvique Peels</div><div class="price">$120</div></div>
    <div class="row"><div class="label">Berry Enzyme Peel</div><div class="price">$120</div></div>
    <div class="row"><div class="label">Fruit Acid Peel</div><div class="price">$120</div></div>
    <div class="row"><div class="label">Hydrating Peel</div><div class="price">$120</div></div>
    <div class="row"><div class="label">Night Retinol Peel</div><div class="price">$250</div></div>
    <div class="gap"></div>
    <h2 class="heading"><span class="mixed">Lumitone <b>LED</b></span></h2>
    <div class="rule"></div>
    <p class="treat"><span class="amt">$90</span> per treatment or<br><span class="amt">$50</span> when added on to any of our other skin treatments.</p>
    <p class="treat"><b>Vitapen Microneedling</b><br>(Collagen Induction Therapy)<br><span class="amt">$350</span> full face<br><span class="amt">$450</span> face, neck and décolletage</p>
    <p class="treat"><b>Veyra Laser Facial</b><br><span class="amt">$350</span> full face<br><span class="amt">$450</span> face, neck and décolletage</p>
    <div class="photo smile" role="img" aria-label="Photo of a smiling woman touching her cheek"></div>
  </div>
</section>

</body>
</html>
```